Letterhead and Business Cards

Using our new logo we would like designs for the following,

1.Letterhead

2. 2 x Business Cards

I will need all three in high quality PDF files ready for printing. I will also require the top and bottom of the letterhead as two JPG files.

Target Market(s)

We are a business to business company dealing with middle to upper management both as clients and suppliers.

Industry/Entity Type

Business

Requirements
Must have
• 1. Look professional.
• 2. Utilise our logo colours
• 3. Incorporate our logo on both.
• 4. Letterhead

• Address:
• Pell Harrow Court
• Pell Harrow Lane
• London
• WC1R 4JZ

• Tel:0845 312 4096
• Fax: 0845 312 7158
• Website: www.kovimerlox.com
• Email: info@kovimerlox.com

• Directors: D.R. Marsh and H.J. Marsh Company Registration No: 52064918(This should be quite small in the letterhead footer somewhere)

• Business Card One Sided Only

• 1. Dominic R. Marsh
• Managing Director

• Address:
• Pell Harrow Court
• Pell Harrow Lane
• London
• WC1R 4JZ

• Tel:0845 312 4096
• Fax: 0845 312 7159
• Mob: 0791 526 3307
• Email: dominic@kovimerlox.com

• 2. Helen J. Marsh
• Sales Director

• Address:
• Pell Harrow Court
• Pell Harrow Lane
• London
• WC1R 4JZ

• Tel:0845 312 4096
• Fax: 0845 312 7158
• Mob: 0794 862 1190
• Email: helen@kovimerlox.com

• Please note some of this info may change for final printing.

```html
<!DOCTYPE html>
<html lang="en">
<head>
<meta charset="utf-8">
<title>Kovimerlox Stationery</title>
<link href="https://fonts.googleapis.com/css2?family=Source+Sans+3:wght@400;600;700&display=swap" rel="stylesheet">
<style>
  :root {
    --green-light: #a2c93a;
    --green-deep: #6db33f;
    --green-text: #5fae3c;
    --grey-line: #9a9a9a;
    --grey-frame: #8c8c8c;
    --ink: #444;
    --brand-grey: #8f8f8f;
    --paper: #ffffff;
  }
  * { margin: 0; padding: 0; box-sizing: border-box; }
  html, body { width: 776px; height: 1200px; overflow: hidden; background: var(--paper); }
  body { position: relative; font-family: "Source Sans 3", "Myriad Pro", sans-serif; color: var(--ink); }

  .sheet { position: absolute; background: var(--paper); border: 0.8px solid var(--grey-frame); overflow: hidden; }
  .sheet svg.backdrop { position: absolute; inset: 0; }
  .letterhead { left: 48px; top: 35px; width: 662px; height: 938px; }
  .card { top: 990px; width: 317px; height: 177px; }
  .card--dominic { left: 41px; }
  .card--helen { left: 398px; }

  .brand { position: absolute; display: flex; align-items: center; }
  .brand__dot { border-radius: 50%; background: var(--green-deep); }
  .brand__name { font-weight: 700; color: var(--brand-grey); letter-spacing: 0.2px; }
  .letterhead .brand { left: 14px; top: 28px; gap: 8px; }
  .letterhead .brand__dot { width: 44px; height: 44px; }
  .letterhead .brand__name { font-size: 24px; }
  .card .brand { left: 7px; top: 14px; gap: 5px; }
  .card .brand__dot { width: 24px; height: 24px; }
  .card .brand__name { font-size: 14px; }

  .lines { position: absolute; list-style: none; letter-spacing: 1.6px; }
  .lines li { white-space: nowrap; }
  .lines .accent { color: var(--green-text); }

  .letterhead .address { left: 12px; top: 866px; font-size: 8.2px; line-height: 16.2px; }
  .letterhead .contact { right: 9px; top: 866px; font-size: 8.2px; line-height: 16.2px; text-align: right; }
  .letterhead .legal { position: absolute; left: 187px; top: 923px; font-size: 5.6px; letter-spacing: 1.1px; }

  .card .person { right: 11px; top: 16px; font-size: 9.2px; line-height: 14px; font-weight: 600; color: #fff; text-align: right; letter-spacing: 2px; }
  .card .address { right: 11px; top: 79px; font-size: 8px; line-height: 14.2px; text-align: right; color: #777; }
  .card .phones { left: 8px; top: 142px; font-size: 6.8px; line-height: 11.4px; color: #777; }
  .card .web { right: 11px; top: 153px; font-size: 6.8px; line-height: 11.4px; text-align: right; }
</style>
</head>
<body>

<section class="sheet letterhead">
  <svg class="backdrop" width="662" height="938" viewBox="0 0 662 938" aria-hidden="true">
    <defs>
      <linearGradient id="lh-band" x1="0" x2="662" y1="0" y2="0" gradientUnits="userSpaceOnUse">
        <stop offset="0.19" stop-color="#ffffff"/>
        <stop offset="0.45" stop-color="#c8df8f"/>
        <stop offset="0.68" stop-color="var(--green-light)"/>
        <stop offset="1" stop-color="var(--green-deep)"/>
      </linearGradient>
    </defs>
    <path d="M0,249 C120,140 300,96 427,96 C520,96 600,108 662,124 V0 H0 Z" fill="url(#lh-band)"/>
    <path d="M0,249 C120,140 300,96 427,96 C520,96 600,108 662,124" fill="none" stroke="var(--grey-line)" stroke-width="1.5"/>
  </svg>
  <div class="brand"><span class="brand__dot"></span><span class="brand__name">Kovimerlox</span></div>

  <ul class="lines address">
    <li>Pell Harrow Court</li>
    <li>Pell Harrow Lane</li>
    <li>London</li>
    <li>WC1R 4JZ</li>
  </ul>
  <p class="legal">Directors: D.R. Marsh and H.J. Marsh Company Registration No: 52064918</p>
  <ul class="lines contact">
    <li>Tel:0845 312 4096</li>
    <li>Fax: 0845 312 7158</li>
    <li>Website: www.kovimerlox.com</li>
    <li class="accent">Email: info@kovimerlox.com</li>
  </ul>
</section>

<section class="sheet card card--dominic">
  <svg class="backdrop" width="317" height="177" viewBox="0 0 317 177" aria-hidden="true">
    <defs>
      <linearGradient id="card-band-a" x1="0" x2="317" y1="0" y2="0" gradientUnits="userSpaceOnUse">
        <stop offset="0.32" stop-color="#ffffff"/>
        <stop offset="0.62" stop-color="var(--green-light)"/>
        <stop offset="1" stop-color="var(--green-deep)"/>
      </linearGradient>
    </defs>
    <path d="M0,135 C60,80 130,52 196,52 C245,52 285,60 317,73 V0 H0 Z" fill="url(#card-band-a)"/>
    <path d="M0,135 C60,80 130,52 196,52 C245,52 285,60 317,73" fill="none" stroke="var(--grey-line)" stroke-width="1.2"/>
  </svg>
  <div class="brand"><span class="brand__dot"></span><span class="brand__name">Kovimerlox</span></div>
  <ul class="lines person">
    <li>Dominic R. Marsh</li>
    <li>Managing Director</li>
  </ul>
  <ul class="lines address">
    <li>Pell Harrow Court</li>
    <li>Pell Harrow Lane</li>
    <li>London</li>
    <li>WC1R 4JZ</li>
  </ul>
  <ul class="lines phones">
    <li>Tel:0845 312 4096</li>
    <li>Fax: 0845 312 7159</li>
    <li>Mob: 0791 526 3307</li>
  </ul>
  <ul class="lines web">
    <li class="accent">Website: www.kovimerlox.com</li>
    <li class="accent">Email: dominic@kovimerlox.com</li>
  </ul>
</section>

<section class="sheet card card--helen">
  <svg class="backdrop" width="317" height="177" viewBox="0 0 317 177" aria-hidden="true">
    <defs>
      <linearGradient id="card-band-b" x1="0" x2="317" y1="0" y2="0" gradientUnits="userSpaceOnUse">
        <stop offset="0.32" stop-color="#ffffff"/>
        <stop offset="0.62" stop-color="var(--green-light)"/>
        <stop offset="1" stop-color="var(--green-deep)"/>
      </linearGradient>
    </defs>
    <path d="M0,135 C60,80 130,52 196,52 C245,52 285,60 317,73 V0 H0 Z" fill="url(#card-band-b)"/>
    <path d="M0,135 C60,80 130,52 196,52 C245,52 285,60 317,73" fill="none" stroke="var(--grey-line)" stroke-width="1.2"/>
  </svg>
  <div class="brand"><span class="brand__dot"></span><span class="brand__name">Kovimerlox</span></div>
  <ul class="lines person">
    <li>Helen J. Marsh</li>
    <li>Sales Director</li>
  </ul>
  <ul class="lines address">
    <li>Pell Harrow Court</li>
    <li>Pell Harrow Lane</li>
    <li>London</li>
    <li>WC1R 4JZ</li>
  </ul>
  <ul class="lines phones">
    <li>Tel:0845 312 4096</li>
    <li>Fax: 0845 312 7158</li>
    <li>Mob: 0794 862 1190</li>
  </ul>
  <ul class="lines web">
    <li class="accent">Website: www.kovimerlox.com</li>
    <li class="accent">Email: helen@kovimerlox.com</li>
  </ul>
</section>

</body>
</html>
```